Box Design for Organic Bamboo Hooded Baby Bath Towels

Box size 25 x 18 x 6cm, attached PDF from supplier for reference, and our logo

We need a box designed for a new company based in Orange County, called Wren Littles & Co. Our company specializes in quality, upscale, health conscious products for infants, babies and toddlers. Our first product launching is a hooded bath towel made of organic bamboo. We would like to see a design that signifies purity, simplicity, safety, and elegance. The colors we like are white, blue (like the shade in our logo attached), greens, and grays.

Front of box:
Needs to include logo

Key Points:
*Unbleached, chemical & toxin free
*Hypoallergenic and Antibacterial
*Three times more absorbent than cotton
*Eco Friendly

Somewhere on the front it needs to note sizing: 30x30 inches
Includes bonus wash cloth

Back of Box:

Do you ever find yourself questioning what products are best for your little one? We thought so. So do we! We are mamas here at Wren Littles & Co, and nothing is more important to us than the well-being of our little ones. 100% organic bamboo is the best of the best for our bundles of joy, being ultra soft, antibacterial, hypoallergenic, free of dyes & chemicals, and 3x more absorbent than cotton. These towels will leave your baby cozy, dry, and happily wrapped up in a silky soft embrace after bath time. From our mama hearts, to yours.

Care Instructions:
-Machine Wash
-Hand Wash
-Do not Dry Clean
-Do not Bleach
-Do not Tumble Dry

Additional Care Tips:
-Wash before first use
-Do not store wet bath towel
-Store in a well aired room (never in a sealed container, plastic bag, etc)
-Avoid contact with rough surfaces which could loosen the yarns
-Do not bleach or use fabric softeners. Dryer sheets are also not recommended
-Keep away from open flames or electric heaters
-If towel is used after swimming pools, sea water, chlorinated water, please be sure to wash immediately after to prevent the bamboo fibre from weakening

Designed in the US, Made in China
Wren Littles & Co
info@wrenlittlesandco.example

Target Market(s)

Moms

Industry/Entity Type

Baby

Font styles to use
Serif
Script

Colors
85cae6
eea4c8
ecf7fb
ffffff
d9d9d9
fdf9cf
cadf82
eaf2ce

Requirements
Must have
• the key info written in project description, our logo, company name, where it's made
Nice to have
• designs that communicate organic, purity & safety
• the yellow & green do not need to be used. If you have an idea and would like to include those colors, we have selected a yellow and two greens that would work with our vision. If you feel otherwise, please let us know why :)
Should not have
• it cannot look busy

```html
<!DOCTYPE html>
<html lang="en">
<head>
<meta charset="utf-8">
<title>Wren Littles &amp; Co — Hooded Baby Towel Box</title>
<link rel="stylesheet" href="https://fonts.googleapis.com/css2?family=Courier+Prime:wght@400;700&family=Oswald:wght@700&display=swap">
<style>
  :root {
    --bg: #f4f6f8;
    --white: #ffffff;
    --sky: #8fd3f0;
    --sky-light: #d6eff9;
    --side-blue: #7db8d9;
    --brand-blue: #1f9cc6;
    --pink: #f29ac6;
    --navy: #243a7a;
    --navy-soft: #3a58a8;
    --panda: #4f7fa8;
  }
  * { margin: 0; padding: 0; box-sizing: border-box; }
  html, body { width: 1200px; height: 864px; overflow: hidden; background: var(--bg); }
  .canvas { position: relative; width: 1200px; height: 864px; }

  .front-panel {
    position: absolute; left: 70px; top: 130px; width: 840px; height: 605px;
    background: var(--white); overflow: hidden;
    box-shadow: 0 6px 24px rgba(30, 60, 90, 0.12);
  }
  .front-panel .wave { position: absolute; inset: 0; }

  .brand-name {
    position: absolute; left: 44px; top: 78px;
    font-family: "Courier Prime", monospace; font-weight: 400;
    font-size: 52px; color: var(--brand-blue); letter-spacing: -1px;
  }

  .baby-photo {
    position: absolute; left: 250px; top: 250px; width: 210px; height: 355px;
    border-radius: 100px 100px 0 0;
    background: linear-gradient(180deg, #f7f7f5 0%, #eedfd6 55%, rgba(143, 211, 240, 0.9) 100%);
  }
  .panda-art {
    position: absolute; left: 590px; top: 190px; width: 96px; height: 100px;
    border-radius: 50%;
    background: radial-gradient(circle at 50% 45%, #7aa3c4 0%, var(--panda) 70%, #3f6a90 100%);
  }

  .features { position: absolute; left: 28px; top: 395px; width: 240px; list-style: none; }
  .feature { display: flex; align-items: center; gap: 8px; margin-bottom: 10px; }
  .feature-icon {
    flex: none; width: 30px; height: 30px; border-radius: 50%;
    background: #6aa6da; display: flex; align-items: center; justify-content: center;
  }
  .feature-label {
    font-family: "Courier Prime", monospace; font-weight: 700; line-height: 1.05;
    color: var(--white); padding: 5px 10px; border-radius: 4px 14px 14px 4px;
    white-space: nowrap;
  }
  .feature-label.eco { background: var(--navy-soft); font-size: 19px; }
  .feature-label.absorb { background: linear-gradient(90deg, #f4a9cf, #a9d7f2); font-size: 13px; }
  .feature-label.clean { background: linear-gradient(90deg, var(--navy-soft), #9cc9ee); font-size: 14px; }

  .product-claims {
    position: absolute; left: 490px; top: 298px; width: 300px; text-align: center;
  }
  .claim-line {
    font-family: "Courier Prime", monospace; font-weight: 700; font-size: 22px;
    color: var(--pink); line-height: 1;
  }
  .product-title {
    margin-top: 12px;
    font-family: "Oswald", sans-serif; font-weight: 700; font-size: 46px;
    line-height: 0.98; color: var(--white); letter-spacing: 1px;
  }
  .product-title .accent { color: var(--pink); }
  .product-size {
    font-family: "Oswald", sans-serif; font-weight: 700; font-size: 38px;
    line-height: 1.1; color: var(--navy); margin-top: 2px;
  }

  .side-panel {
    position: absolute; left: 910px; top: 130px; width: 202px; height: 605px;
    background: var(--side-blue); overflow: hidden;
    box-shadow: 0 6px 24px rgba(30, 60, 90, 0.12);
  }
  .side-text {
    position: absolute; left: 50%; top: 50%;
    transform: translate(-50%, -50%) rotate(-90deg);
    white-space: nowrap; text-align: center;
  }
  .side-brand {
    font-family: "Courier Prime", monospace; font-size: 30px;
    color: var(--brand-blue); margin-bottom: 14px;
  }
  .side-bonus {
    font-family: "Oswald", sans-serif; font-weight: 700; font-size: 36px;
    line-height: 1; color: var(--navy);
  }
</style>
</head>
<body>
<main class="canvas">
  <section class="front-panel" aria-label="Box front">
    <svg class="wave" viewBox="0 0 840 605" aria-hidden="true">
      <path d="M0 300 C180 350 400 330 560 275 S760 190 840 160" fill="none" stroke="var(--sky)" stroke-width="10"/>
      <path d="M0 345 C200 385 420 360 580 310 S770 225 840 205 L840 605 L0 605 Z" fill="var(--sky)"/>
    </svg>

    <div class="brand-name">Wren Littles &amp; Co</div>

    <div class="baby-photo" role="img" aria-label="Photo of a baby wrapped in a white hooded bath towel"></div>
    <div class="panda-art" role="img" aria-label="Illustration of a blue panda holding bamboo leaves"></div>

    <ul class="features">
      <li class="feature">
        <span class="feature-icon"><svg width="16" height="16" viewBox="0 0 16 16"><path d="M2 14 C2 6 8 2 14 2 C14 9 9 14 2 14 Z" fill="#fff"/></svg></span>
        <span class="feature-label eco">Eco Friendly</span>
      </li>
      <li class="feature">
        <span class="feature-icon"><svg width="16" height="16" viewBox="0 0 16 16"><path d="M8 2 C11 6 12 8 12 10 A4 4 0 0 1 4 10 C4 8 5 6 8 2 Z" fill="#fff"/></svg></span>
        <span class="feature-label absorb">Three times more<br>absorbent than cotton</span>
      </li>
      <li class="feature">
        <span class="feature-icon"><svg width="16" height="16" viewBox="0 0 16 16"><path d="M3 3 L13 13 M13 3 L3 13" stroke="#fff" stroke-width="2.5" stroke-linecap="round"/></svg></span>
        <span class="feature-label clean">Unbleached, chemical<br>&amp; toxin free</span>
      </li>
    </ul>

    <div class="product-claims">
      <p class="claim-line">Hypoallergenic</p>
      <p class="claim-line">and</p>
      <p class="claim-line">Antibacterial</p>
      <h1 class="product-title">HOODED<br><span class="accent">BABY</span><br>TOWEL</h1>
      <p class="product-size">30x30"</p>
    </div>
  </section>

  <section class="side-panel" aria-label="Box side">
    <div class="side-text">
      <p class="side-brand">Wren Littles &amp; Co</p>
      <p class="side-bonus">INCLUDES BONUS<br>WASH CLOTH</p>
    </div>
  </section>
</main>
</body>
</html>
```